Business Card Design Project

We need a Business Card for an Mechanical Engineering firm in Singapore. The design should be Modern & Technical looking, yet eye catching.

Our company deals in Cutting Tools & Machine Accessories for the Manufacturing Industries such as Oil & Gas, Aero Space, etc... For more information on our Company, you can either email me or view our website www.torvale.com.sg.

We are trying to revamp our image to give our consumers a fresh new perspective to our company, so we welcome all ideas.

Industry/Entity Type

Business

Requirements
Must have
• Must incorporate New Company Logo into the card as shown in Uploaded file.

```html
<!DOCTYPE html>
<html lang="en">
<head>
<meta charset="utf-8">
<title>Torvale Tools – Business Card</title>
<link rel="stylesheet" href="https://fonts.googleapis.com/css2?family=Lato:wght@400;700&display=swap">
<style>
  :root {
    --crimson: #9b0b37;
    --ink: #2f2f33;
    --ink-soft: #4a4a50;
    --paper: #ffffff;
    --backdrop: #d6dadd;
  }
  * { box-sizing: border-box; margin: 0; padding: 0; }
  html, body {
    width: 1200px;
    height: 960px;
    overflow: hidden;
    background: var(--backdrop);
    font-family: "Lato", sans-serif;
  }
  .card-sheet {
    width: 1200px;
    height: 960px;
    display: flex;
    flex-direction: column;
    align-items: center;
    justify-content: center;
    gap: 44px;
  }
  .card {
    position: relative;
    width: 700px;
    height: 400px;
    border-radius: 4px;
    box-shadow: 0 10px 28px rgba(0, 0, 0, 0.18);
    overflow: hidden;
  }
  .card--front { background: var(--paper); color: var(--ink); }
  .card--back {
    background: var(--crimson);
    display: flex;
    align-items: center;
    justify-content: center;
  }

  .holder { position: absolute; left: 50px; top: 64px; }
  .holder__name { font-size: 38px; font-weight: 400; letter-spacing: 0.2px; }
  .holder__role { font-size: 21px; margin-top: 6px; color: var(--ink-soft); }

  .contacts {
    position: absolute; left: 50px; top: 200px;
    list-style: none;
    font-size: 18px;
    line-height: 28px;
    color: var(--ink-soft);
  }
  .contacts li { display: flex; align-items: center; gap: 14px; }
  .contacts svg { width: 14px; height: 14px; flex: none; }
  .contacts__web { font-weight: 700; color: var(--ink); }

  .address {
    position: absolute; left: 50px; top: 300px;
    font-size: 18px; line-height: 26px; color: var(--ink-soft);
    font-style: normal;
  }

  .brand { display: flex; align-items: center; gap: 12px; font-weight: 700; text-transform: uppercase; }
  .brand__dot { border-radius: 50%; flex: none; }
  .card--front .brand {
    position: absolute; right: 44px; bottom: 70px;
    color: var(--crimson); font-size: 32px; letter-spacing: 1px;
  }
  .card--front .brand__dot { width: 22px; height: 22px; background: var(--crimson); }
  .card--back .brand { color: var(--paper); font-size: 48px; letter-spacing: 2px; }
  .card--back .brand__dot { width: 30px; height: 30px; background: var(--paper); }
</style>
</head>
<body>
<main class="card-sheet">

  <section class="card card--front" aria-label="Business card front">
    <div class="holder">
      <h1 class="holder__name">Arjun Mehta</h1>
      <p class="holder__role">Operations Director</p>
    </div>

    <ul class="contacts">
      <li>
        <svg viewBox="0 0 14 14" aria-hidden="true"><rect x="3" y="0.5" width="8" height="13" rx="1.5" fill="var(--crimson)"/><rect x="4.5" y="2.5" width="5" height="5" fill="#fff"/></svg>
        <span>65-61234578</span>
      </li>
      <li>
        <svg viewBox="0 0 14 14" aria-hidden="true"><rect x="0.5" y="2.5" width="13" height="9" fill="var(--crimson)"/><path d="M1 3.2 L7 8 L13 3.2" fill="none" stroke="#fff" stroke-width="1.3"/></svg>
        <span>mail@torvale.com.sg</span>
      </li>
      <li>
        <svg viewBox="0 0 14 14" aria-hidden="true"><circle cx="7" cy="7" r="6.5" fill="var(--crimson)"/><path d="M1 7 H13 M7 1 C4 4 4 10 7 13 M7 1 C10 4 10 10 7 13" fill="none" stroke="#fff" stroke-width="1"/></svg>
        <span class="contacts__web">www.torvale.com.sg</span>
      </li>
    </ul>

    <address class="address">
      27 Kallang Way #03-12,<br>
      Northpoint Works Hub,<br>
      Singapore 349211
    </address>

    <div class="brand"><span>Torvale Tools</span><span class="brand__dot" aria-hidden="true"></span></div>
  </section>

  <section class="card card--back" aria-label="Business card back">
    <div class="brand"><span>Torvale Tools</span><span class="brand__dot" aria-hidden="true"></span></div>
  </section>

</main>
</body>
</html>
```